Wirenexa

I'm looking to much improve our current website wirenexa.com
Updates

Low design quality

Target Market(s)

Commercial clients (Not-Residentials)

Industry/Entity Type

Office buildings and Industrial clients

Coding

Coded - Design and coding required

Number of Pages Required

5+ page

Requirements
Must have
• Very professional structured low voltage cabling projects for Wi-Fi, Audio/Video conference rooms, Access Control systems, CCTV.

```html
<!DOCTYPE html>
<html lang="en">
<head>
<meta charset="utf-8">
<title>Wirenexa — Professional Low Voltage Cabling</title>
<link rel="stylesheet" href="https://fonts.googleapis.com/css2?family=Oswald:wght@400;500;600&family=Inter:wght@400;500;600;700&display=swap">
<style>
:root{
  --red:#e0282a;
  --red-deep:#c91f21;
  --ink:#ffffff;
  --muted:#c9c9c9;
  --bg-deep:#111111;
  --bg-mid:#1d1d1d;
  --bg-strip:#262626;
  --card:#2a2a2a;
  --field:#0d0d0d;
}
*{box-sizing:border-box;margin:0;padding:0}
html,body{width:1200px;height:4399px;overflow:hidden;background:var(--bg-deep);color:var(--ink);font-family:"Inter",sans-serif}
.page{position:relative;width:1200px;height:4399px;overflow:hidden}
section,footer{position:absolute;left:0;width:1200px}
.abs{position:absolute}
.title{font-family:"Oswald",sans-serif;font-weight:500;text-transform:uppercase;letter-spacing:.5px;font-size:29px}
.title .accent{color:var(--red)}
.btn{position:absolute;background:var(--red);color:#fff;font-size:12px;font-weight:700;text-transform:uppercase;display:flex;align-items:center;justify-content:center;letter-spacing:.3px}
.photo{position:absolute}

/* hero */
.hero{top:0;height:632px;background:#0b0b0f}
.hero .photo{inset:0;background:radial-gradient(circle at 30% 40%,#6b3a2a 0%,rgba(0,0,0,0) 45%),radial-gradient(circle at 80% 30%,#ff6a1a 0%,rgba(0,0,0,0) 35%),radial-gradient(circle at 65% 80%,#9b2fd1 0%,rgba(0,0,0,0) 40%),linear-gradient(120deg,#1a0f12,#2b1434 60%,#130a18)}
.nav{left:128px;top:26px;width:944px;height:63px;background:#141414;clip-path:polygon(4% 0,100% 0,96% 100%,0 100%)}
.brand{font-family:"Oswald",sans-serif;font-weight:600;font-size:31px;display:flex;align-items:center;gap:8px;color:#fff}
.brand .mark{width:26px;height:26px;background:var(--red)}
.nav .brand{position:absolute;left:42px;top:13px}
.menu{position:absolute;left:320px;top:25px;display:flex;gap:40px;font-size:10px;font-weight:500;text-transform:uppercase}
.menu .on{color:var(--red)}
.callus{position:absolute;left:784px;top:17px;font-size:11px;font-weight:600}
.callus small{display:block;color:var(--red);font-size:8px;margin-bottom:3px}
.slide-dots{left:24px;top:276px;width:16px}
.hero-card{left:669px;top:324px;width:403px;height:226px;background:var(--red);clip-path:polygon(0 0,100% 0,100% 88%,90% 100%,0 100%);padding:32px 20px 0 33px}
.hero-card h1{font-family:"Oswald",sans-serif;font-weight:500;font-size:19px;line-height:29px;text-transform:uppercase;letter-spacing:.3px;white-space:nowrap}
.perks{display:flex;gap:20px;margin-top:16px;font-family:"Oswald",sans-serif;font-size:11px;text-transform:uppercase}
.perks span{display:flex;align-items:center;gap:6px}
.perks i{width:13px;height:13px;border:1.5px solid #fff;border-radius:50%;display:inline-block}

/* trusted */
.trusted{top:632px;height:110px;background:var(--bg-strip);display:flex;align-items:center;gap:42px;padding-left:128px;color:#9a9a9a;white-space:nowrap}
.trusted .label{font-size:8px;letter-spacing:.5px}
.partner{display:flex;align-items:center;gap:7px;font-weight:700;font-size:15px}
.partner b{width:20px;height:20px;background:#8a8a8a;border-radius:50%;display:inline-block}

/* about */
.about{top:742px;height:513px;background:var(--bg-mid)}
.about .title{left:128px;top:78px}
.about p{left:128px;top:134px;width:326px;font-size:11.5px;line-height:17.5px;color:#e4e4e4}
.frame-red{position:absolute;background:var(--red)}

/* services */
.services{top:1255px;height:695px;background:var(--bg-deep)}
.center{width:100%;text-align:center}
.svc{position:absolute;top:172px;width:461px;height:345px}
.svc .tag{position:absolute;left:38px;top:239px;background:var(--red);font-size:11px;font-weight:700;padding:9px 20px;text-transform:uppercase}
.svc p{position:absolute;left:38px;top:283px;width:300px;font-size:11.5px;line-height:17px}
.arrow{position:absolute;top:328px;width:40px;height:40px;border-radius:50%;background:#2f2f2f;display:flex;align-items:center;justify-content:center}

/* expertise */
.expertise{top:1950px;height:597px;background:var(--bg-mid)}
.exp{position:absolute;width:297px;height:86px;background:var(--card);display:flex;align-items:center;justify-content:center;padding-top:22px;font-size:11.5px;font-weight:700}
.exp .ico{position:absolute;left:128px;top:-22px;width:42px;height:42px;border-radius:50%;background:var(--red);display:flex;align-items:center;justify-content:center;border:3px solid #f4b3b3}

/* features */
.features{top:2547px;height:585px;background:var(--bg-deep)}
.features .title{left:753px;top:115px}
.feat{position:absolute;left:751px;width:330px;display:flex;gap:14px}
.feat .ico{flex:none;width:40px;height:40px;border-radius:50%;background:var(--red);border:3px solid #f4b3b3}
.feat h4{color:var(--red);font-size:11.5px;font-weight:600;margin-bottom:2px}
.feat p{font-size:11px;line-height:17px;color:#e6e6e6}

/* testimonials */
.testimonials{top:3132px;height:632px;background:var(--bg-mid)}
.quote-mark{font-family:"Oswald",sans-serif;font-size:120px;line-height:1;color:var(--red);font-weight:600}
.tcard{position:absolute;top:171px;width:297px;height:103px;background:var(--card);padding:18px 20px;font-size:11.5px;line-height:18px;color:#eaeaea}
.tname{position:absolute;font-size:11.5px;line-height:17px}
.tname span{color:var(--red);display:block}
.dots{left:0;top:396px;width:100%;display:flex;justify-content:center;gap:7px;align-items:center}
.dots i{width:4px;height:4px;border-radius:50%;background:#aaa;display:block}
.dots i.on{width:9px;height:9px;border:2px solid #ddd;background:none}

/* callback */
.callback-box{left:126px;top:3629px;width:946px;height:283px;background:#232323}
.callback-red{left:126px;top:3629px;width:432px;height:283px;background:var(--red-deep);padding:42px 0 0 48px}
.callback-red h2{font-family:"Oswald",sans-serif;font-weight:500;font-size:33px;line-height:44px;text-transform:uppercase}
.callback-red h2 .dark{color:#1a1a1a}
.callback-red p{font-size:12.5px;margin-top:14px}
.field{position:absolute;background:var(--field);font-size:11px;padding:12px 11px;color:#e0e0e0}

/* footer */
.footer{top:3912px;height:487px;background:var(--bg-deep)}
.fcol{position:absolute;top:84px;font-size:10.5px;line-height:22px;color:#e0e0e0}
.fcol h5{font-size:10px;font-weight:500;color:#9a9a9a;text-transform:uppercase;margin-bottom:20px;letter-spacing:.3px}
.badge{position:absolute;left:185px;top:190px;width:85px;height:60px;border-radius:8px;background:linear-gradient(90deg,#7a3bd6,#e0282a,#f4b12e,#2fae5e)}
.rule{left:128px;top:350px;width:944px;height:1px;background:#333}
.copy{left:128px;top:376px;font-size:9px;color:#9a9a9a;letter-spacing:.3px}
.social{right:128px;top:372px;display:flex;gap:12px}
.social i{width:13px;height:13px;border-radius:50%;background:#fff;display:block}
</style>
</head>
<body>
<div class="page">

<section class="hero">
  <div class="photo" role="img" aria-label="Technician organizing colorful network cables in a server rack under orange and purple light"></div>
  <div class="abs nav">
    <div class="brand"><span class="mark"></span>Wirenexa</div>
    <nav class="menu"><span class="on">Home</span><span>About Us</span><span>Services ⌄</span><span>Key Features</span><span>Contact</span></nav>
    <div class="callus"><small>CALL US TODAY</small>✆ (888)-555-0142</div>
  </div>
  <svg class="abs slide-dots" width="16" height="80" viewBox="0 0 16 80"><rect x="2" y="0" width="12" height="16" rx="3" fill="none" stroke="#fff" stroke-width="1.5"/><circle cx="8" cy="38" r="4" fill="none" stroke="#fff"/><circle cx="8" cy="38" r="1.8" fill="#fff"/><circle cx="8" cy="50" r="1.3" fill="#fff"/><circle cx="8" cy="59" r="1.3" fill="#fff"/><circle cx="8" cy="68" r="1.3" fill="#fff"/></svg>
  <div class="abs hero-card">
    <h1>Professional cabling for<br>computers, security cameras,<br>Wi-Fi, VoIP phones, access control,<br>video and audio, serving Virginia,<br>Washington DC and Maryland.</h1>
    <div class="perks"><span><i></i>Safe &amp; Secure</span><span><i></i>24x7 Support</span><span><i></i>Low Cost</span></div>
  </div>
</section>

<section class="trusted">
  <span class="label">TRUSTED BY</span>
  <span class="partner"><b></b>Northwind</span>
  <span class="partner"><b></b>Terragen</span>
  <span class="partner"><b></b>Coastcity</span>
  <span class="partner">Ridgeway</span>
  <span class="partner"><b></b>Bayport</span>
  <span class="partner"><b></b>Stonebuild</span>
  <span class="partner"><b></b>reclaimworks</span>
  <span class="partner">Veltra</span>
</section>

<section class="about">
  <h2 class="abs title"><span class="accent">About</span> Wirenexa</h2>
  <p class="abs">Wirenexa is your premier provider of professional low voltage cabling services in Virginia, Washington DC, and Maryland. With a focus on quality, reliability, and attention to detail, we deliver exceptional cabling solutions for audio, video, security systems, computer networks, and more.</p>
  <div class="btn" style="left:126px;top:259px;width:155px;height:36px">More About Us</div>
  <div class="frame-red" style="left:536px;top:60px;width:182px;height:338px;clip-path:polygon(0 0,100% 0,100% 4%,4% 100%,0 100%)"></div>
  <div class="photo" role="img" aria-label="Technician in hard hat and goggles working with red and blue cables" style="left:550px;top:72px;width:440px;height:316px;background:linear-gradient(135deg,#1d3550,#2b5e86 45%,#8a2a33)"></div>
  <div class="photo" role="img" aria-label="Hands holding a bundle of white network cables" style="left:833px;top:234px;width:239px;height:185px;background:linear-gradient(135deg,#213a6b,#4a79b5 50%,#4a1f22);border:6px solid var(--bg-mid)"></div>
</section>

<section class="services">
  <h2 class="title center" style="position:absolute;top:100px"><span class="accent">Our</span> Services</h2>
  <div class="svc" style="left:126px">
    <div class="photo" role="img" aria-label="Technician in orange hard hat with laptop among colorful data cables" style="inset:0;background:linear-gradient(150deg,#6b4a2a,#3a4a5c 50%,#1c2230)"></div>
    <div class="tag">Commercial Services</div>
    <p>Complete office low voltage cabling and Wi-Fi for your network and security system.</p>
  </div>
  <div class="svc" style="left:613px">
    <div class="photo" role="img" aria-label="Technician in blue hard hat inspecting a lit patch panel" style="inset:0;background:linear-gradient(150deg,#b8461f,#3a3aa8 45%,#1a2340)"></div>
    <div class="tag">Industrial Services</div>
    <p>Structured cabling, IDF and MDF for warehouses, manufacturing facilities and others.</p>
  </div>
  <div class="arrow" style="left:106px"><svg width="14" height="14" viewBox="0 0 14 14"><path d="M13 7H2M6 2L1 7l5 5" stroke="#fff" stroke-width="1.8" fill="none"/></svg></div>
  <div class="arrow" style="left:1054px"><svg width="14" height="14" viewBox="0 0 14 14"><path d="M1 7h11M8 2l5 5-5 5" stroke="#fff" stroke-width="1.8" fill="none"/></svg></div>
  <div class="btn" style="left:513px;top:564px;width:174px;height:35px">View All Services</div>
</section>

<section class="expertise">
  <h2 class="title center" style="position:absolute;top:100px"><span class="accent">Wirenexa</span> Expertise</h2>
  <div class="exp" style="left:126px;top:194px"><span class="ico"></span>Voice &amp; Data Cable Installations</div>
  <div class="exp" style="left:451px;top:194px"><span class="ico"></span>Copper Cable CAT6 and CAT7</div>
  <div class="exp" style="left:777px;top:194px"><span class="ico"></span>Fiber Cable Single &amp; Multi Mode</div>
  <div class="exp" style="left:126px;top:332px"><span class="ico"></span>Conduit Installations</div>
  <div class="exp" style="left:451px;top:332px"><span class="ico"></span>IDF and MDF Installations</div>
  <div class="exp" style="left:777px;top:332px"><span class="ico"></span>Linktest LX-8000 Certification</div>
  <div class="btn" style="left:517px;top:465px;width:167px;height:38px">Request a Quote</div>
</section>

<section class="features">
  <div class="frame-red" style="left:126px;top:95px;width:180px;height:330px;clip-path:polygon(0 0,100% 0,100% 4%,4% 100%,0 100%)"></div>
  <div class="photo" role="img" aria-label="Technician patching red network cables in a server rack" style="left:140px;top:109px;width:440px;height:314px;background:linear-gradient(135deg,#2b2b2b,#7a2a1e 50%,#c24a20)"></div>
  <div class="photo" role="img" aria-label="Hand connecting blue patch cables to a switch" style="left:417px;top:303px;width:245px;height:182px;background:linear-gradient(135deg,#13233e,#2e5fa8 55%,#0c1424);border:6px solid var(--bg-deep)"></div>
  <h2 class="abs title"><span class="accent">Key Features of</span> Wirenexa</h2>
  <div class="feat" style="top:176px"><span class="ico"></span><div><h4>Expertise and Experience</h4><p>With years of experience in the industry, we bring a wealth of expertise to every project.</p></div></div>
  <div class="feat" style="top:242px"><span class="ico"></span><div><h4>Comprehensive Solutions</h4><p>From copper CAT6 and CAT7 cabling to fiber optic installations, we offer them all.</p></div></div>
  <div class="feat" style="top:308px"><span class="ico"></span><div><h4>Quality Workmanship</h4><p>At Wirenexa, we take pride in our work and strive for excellence in all project we undertake.</p></div></div>
  <div class="feat" style="top:374px"><span class="ico"></span><div><h4>Commercial and Industrial</h4><p>From office buildings to data centers, we have the capabilities to handle diverse requirements.</p></div></div>
  <div class="feat" style="top:440px"><span class="ico"></span><div><h4>Customer Satisfaction</h4><p>Our commitment to customer satisfaction drives everything we do.</p></div></div>
</section>

<section class="testimonials">
  <div class="abs" style="left:395px;top:72px;display:flex;align-items:center;gap:16px">
    <span class="quote-mark" style="height:62px;overflow:hidden;line-height:.9">“</span>
    <h2 class="title"><span class="accent">Client</span> Testimonials</h2>
  </div>
  <div class="tcard" style="left:126px">"There were zero items identified at the audit, and no further action is required."</div>
  <div class="tcard" style="left:451px">"The site came up extremely well for the outcome and I was very pleased with the outcome."</div>
  <div class="tcard" style="left:777px">"Management of subcontractors on a remote site was above the expected standard."</div>
  <div class="tname" style="left:146px;top:288px">Contract Manager,<span>Government Client</span></div>
  <div class="tname" style="left:469px;top:307px">Maintenance Contract Supervisor,<span>Government Client</span></div>
  <div class="tname" style="left:790px;top:288px">Superintendent's Representative,<span>Government Client</span></div>
  <div class="abs dots"><i class="on"></i><i></i><i></i><i></i><i></i></div>
</section>

<div class="abs callback-box"></div>
<div class="abs callback-red">
  <h2>Engage with <span class="dark">Wirenexa</span><br>&amp; Request a Callback</h2>
  <p>Submit the form and we will contact you within 1 hour.</p>
</div>
<div class="field" style="left:603px;top:3665px;width:208px;height:38px">First Name</div>
<div class="field" style="left:821px;top:3665px;width:208px;height:38px">Last Name</div>
<div class="field" style="left:603px;top:3712px;width:208px;height:38px">Email</div>
<div class="field" style="left:821px;top:3712px;width:208px;height:38px">Phone</div>
<div class="field" style="left:603px;top:3759px;width:426px;height:72px">Message</div>
<div class="btn" style="left:603px;top:3842px;width:208px;height:36px">Send</div>

<footer class="footer">
  <div class="brand abs" style="left:126px;top:74px;font-size:36px"><span class="mark" style="width:30px;height:30px"></span>Wirenexa</div>
  <div class="badge" role="img" aria-label="30th anniversary badge"></div>
  <div class="fcol" style="left:422px"><h5>Navigation</h5>Home<br>About Us<br>Services<br>Key Features<br>Contact</div>
  <div class="fcol" style="left:572px"><h5>Services</h5>Commercial<br>Industrial<br>Residential</div>
  <div class="fcol" style="left:717px"><h5>Main Office - VA</h5>⌖ 4410 Larkfield Road<br>&nbsp;&nbsp;&nbsp;Suite 210<br>&nbsp;&nbsp;&nbsp;Vienna, VA 22180<br><br>✆ (888) 555-0142 (National)<br>&nbsp;&nbsp;&nbsp;(703) 555-0187 (Local)<br><br>✉ sales@wirenexa.com</div>
  <div class="fcol" style="left:947px"><h5>Regional Office - MD</h5>1275 Harbor Crest Way<br>Suite 300<br>Bethesda, MD, 20814</div>
  <div class="abs rule"></div>
  <div class="abs copy">COPYRIGHT © 2025 WIRENEXA. ALL RIGHTS RESERVED.</div>
  <div class="abs social"><i></i><i></i><i></i><i></i></div>
</footer>

</div>
</body>
</html>
```